【依頼の目的/概要】
電子書籍(pavlo)の表紙デザインをお願いします

【画像サイズ】
*RVSより抜粋
表紙ファイルの理想的な寸法は2,560×1,600ピクセルです。
注:画像の寸法は1,000×625ピクセル以上であることが必要です
画像の最大の寸法は10,000×10,000ピクセルです

【タイトル】
朝の庭で見つけた小さな灯りの話

サブキャッチ
~来場者2倍、満足度9割の老舗書店を育てた5つの習慣

【著者】
ミドリノタネ工房代表
組織進化コンサルタント
柳瀬 公平

【本の内容】
とても勤勉で勉強家の開業歯科医のみなさんが
がんばってもなかなか成果の出づらい分野、
「チーム創り」について。

まず互いを人として大事にすることで
スタッフが自然に結束し、
「ここで働けてよかった」
と思うようになる。
楽しいから自主的創造的に動くようになる。
すると成果の質も高くなる。
そうなるまでのステップを紹介。

著者はレポートを出す型のコンサルではなく、
現場に入り込んでゲーム性の高い体験型研修や
一人一人の話を聴いて言葉にならない本音を通訳することなどが得意。
愛と遊び心をもってプログラムを提供し伴走するので
笑顔が絶えることがない。

*参考資料として原稿を添付します

【デザイン要望】
特にイメージにこだわりはありませんので
自由な発想でのデザインご応募を楽しみにしています。

*次点、次々点の方への参加報酬を設定いたしました。

*その他、必要な情報がありましたらお問い合わせください。

スマホでpavloを見るとき、小さなアイコンが並ぶ中で最も目に留まるデザインで、
一目で重要なワードも目に入るデザインだったので採用させていただきました。

次点の二つについても同様の基準でしたが
色使いやフォントサイズなどを調整して、
もっとパッと目に入るものでしたら順序が変わったかもしれません。

特に、チームがテーマなので人の写真+見やすいデザインが両方だったらよりよかったかなと思います

皆さま、一所懸命やっていただいてありがとうございました。
こんなにもたくさんの方にご提案いただけてとてもうれしいです。
お礼を出せるのは3作品ですが
皆様にお礼を改めて申し上げたいと思います。

電子書籍の売れ行きにとても大事な表紙づくりのご協力、本当にありがとうございました。

```html
<!DOCTYPE html>
<html lang="ja">
<head>
<meta charset="utf-8">
<title>朝の庭で見つけた小さな灯りの話</title>
<link rel="stylesheet" href="https://fonts.googleapis.com/css2?family=Noto+Sans+JP:wght@400;500;700;900&family=Roboto+Condensed:wght@400&display=swap">
<style>
  :root {
    --blue: #2b7fd4;
    --blue-light: #8fbde8;
    --ink: #1b1b1f;
    --grey: #6c6f75;
    --panel: #e8edf2;
    --white: #ffffff;
    --yellow: #ffe45c;
  }
  * { margin: 0; padding: 0; box-sizing: border-box; }
  html, body { width: 750px; height: 1200px; overflow: hidden; background: var(--white); }
  .cover {
    position: relative; width: 750px; height: 1200px; overflow: hidden;
    font-family: "Noto Sans JP", sans-serif; color: var(--ink); background: var(--white);
  }
  .audience-badge {
    position: absolute; left: 100px; top: 20px; width: 180px; height: 180px;
    border: 3px solid var(--blue-light); border-radius: 50%;
    display: flex; flex-direction: column; align-items: center; justify-content: center;
    color: var(--blue); font-weight: 700; font-size: 30px; line-height: 1.15; text-align: center;
    background: var(--white);
  }
  .audience-badge .tooth-icon {
    position: absolute; top: -22px; left: 62px; width: 50px; height: 44px;
    background: var(--white); border-radius: 12px;
  }
  .audience-badge .line-wide { letter-spacing: 0.35em; margin-right: -0.35em; }
  .author-figure {
    position: absolute; left: 325px; top: 0; width: 150px; height: 238px;
    background: linear-gradient(180deg, #eef3f8 0%, #d9e4ef 100%);
    border-radius: 0 0 70px 70px;
  }
  .author-block { position: absolute; left: 498px; top: 48px; }
  .author-role { font-size: 15px; font-weight: 700; line-height: 1.45; color: var(--ink); }
  .author-name { margin-top: 8px; font-size: 34px; font-weight: 700; color: var(--blue); letter-spacing: 0.05em; }
  .author-name small { font-size: 22px; margin-left: 6px; }
  .title-frame { position: absolute; left: 0; top: 0; }
  .title {
    position: absolute; left: 55px; top: 262px; width: 640px;
    text-align: center; font-weight: 900; line-height: 1.13;
  }
  .title .line { display: block; font-size: 88px; white-space: nowrap; }
  .title .sub { font-size: 64px; }
  .title .accent { color: var(--blue); }
  .title-english {
    position: absolute; left: 0; width: 750px; top: 590px; text-align: center;
    font-family: "Roboto Condensed", sans-serif; font-size: 17px; color: var(--grey);
  }
  .panel { position: absolute; left: 0; top: 645px; width: 750px; height: 555px; background: var(--panel); }
  .promise {
    position: absolute; left: 0; width: 750px; top: 62px; text-align: center;
    font-size: 44px; font-weight: 900; letter-spacing: 0.01em;
  }
  .promise .accent { color: var(--blue); font-size: 50px; }
  .results-badge {
    position: absolute; left: 20px; top: 210px; width: 190px; height: 190px; border-radius: 50%;
    background: var(--blue); color: var(--white); font-weight: 900;
    display: flex; flex-direction: column; align-items: center; justify-content: center; line-height: 1;
  }
  .results-badge .row { display: flex; align-items: baseline; gap: 6px; }
  .results-badge .label { font-size: 24px; }
  .results-badge .value { font-size: 58px; color: var(--yellow); }
  .results-badge .unit { font-size: 30px; color: var(--yellow); }
  .results-badge .row + .row { margin-top: 6px; }
  .habits { position: absolute; left: 445px; top: 170px; width: 290px; }
  .habits-lead { position: relative; text-align: center; font-weight: 900; font-size: 38px; line-height: 1.35; }
  .habits-lead .dotted span { position: relative; }
  .habits-lead .dotted span::before {
    content: ""; position: absolute; top: -4px; left: 50%; width: 6px; height: 6px;
    margin-left: -3px; border-radius: 50%; background: var(--ink);
  }
  .habits-count { display: flex; align-items: flex-end; justify-content: center; margin-top: -6px; font-weight: 900; }
  .habits-count .number { font-size: 190px; line-height: 0.85; color: var(--blue); }
  .habits-count .word { font-size: 40px; margin-left: 6px; margin-bottom: 6px; }
  .habits-brackets { position: absolute; left: 0; top: 0; }
</style>
</head>
<body>
<main class="cover">
  <div class="audience-badge">
    <div class="tooth-icon" role="img" aria-label="歯のアイコン"></div>
    <span class="line-wide">開業</span>
    <span>歯科医</span>
    <span>のための</span>
  </div>

  <div class="author-figure" role="img" aria-label="白衣姿で指を立てる著者のイラスト"></div>

  <div class="author-block">
    <p class="author-role">ミドリノタネ工房代表</p>
    <p class="author-role">組織進化コンサルタント</p>
    <p class="author-name">柳瀬 公平<small>著</small></p>
  </div>

  <svg class="title-frame" width="750" height="640" viewBox="0 0 750 640" aria-hidden="true">
    <g fill="none" stroke="var(--blue)" stroke-width="3">
      <polyline points="320,238 55,238 55,600 90,600"/>
      <polyline points="480,238 695,238 695,600 660,600"/>
    </g>
  </svg>

  <h1 class="title">
    <span class="line"><span class="sub">朝の庭で</span><span class="accent">見つけた</span></span>
    <span class="line"><span class="accent">小さな</span>灯り</span>
    <span class="line">の話</span>
  </h1>
  <p class="title-english">A Story of the Small Light Found in the Morning Garden.</p>

  <section class="panel">
    <p class="promise">「人にも<span class="accent">お金</span>にも困らない」</p>

    <div class="results-badge">
      <div class="row"><span class="label">来場者</span><span class="value">2</span><span class="unit">倍</span></div>
      <div class="row"><span class="label">満足度</span><span class="value">9</span><span class="unit">割</span></div>
    </div>

    <div class="habits">
      <svg class="habits-brackets" width="290" height="130" viewBox="0 0 290 130" aria-hidden="true">
        <g stroke="var(--ink)" stroke-width="3">
          <line x1="2" y1="20" x2="24" y2="112"/>
          <line x1="288" y1="20" x2="266" y2="112"/>
        </g>
      </svg>
      <p class="habits-lead"><span class="dotted"><span>老</span><span>舗</span><span>書</span><span>店</span></span><br>を育てた</p>
      <p class="habits-count"><span class="number">5</span><span class="word">つの習慣</span></p>
    </div>
  </section>
</main>
</body>
</html>
```